Maplerise Trading Inc. needs an innovative idea for letterhead and visiting cards.

Maplerise Trading Inc. is a Canadian brand since 2007. It is a renown dealer of kids and office furniture locally. Moreover, exporting electric fixtures e.g. switches, LED's, down-lights etc. to Middle East and Africa. We have initiated a number of steps including re-branding, to boost our export in 2020. We have successfully designed our new logo a few months ago through 'Artfolio' and now we are looking for an innovative idea for a letterhead.
Some key points:
• Red, black and white are the three colors used in all our packaging and furniture. (grey is optional)
• Shouldn’t be too wide.
• Use of watermark is preferable.
• You can visit our North American site at www.mapleriseinc.com. Export website of the company will be launched soon. www.mapleriseinc.ca
• Same letterhead will be used locally and internationally.
• Our new logo and sample packaging is attached.

```html
<!DOCTYPE html>
<html lang="en">
<head>
<meta charset="utf-8">
<title>Maplerise Trading Inc. — Letterhead</title>
<link href="https://fonts.googleapis.com/css2?family=Lato:wght@400;700&display=swap" rel="stylesheet">
<style>
  :root {
    --backdrop: #e9e9ea;
    --paper: #f4f4f3;
    --brand-red: #a91d22;
    --ink-grey: #4a4a4c;
    --soft-grey: #5b5b5d;
    --watermark: #dcdcdc;
  }
  * { box-sizing: border-box; margin: 0; padding: 0; }
  html, body {
    width: 1200px; height: 795px; overflow: hidden;
    background: var(--backdrop);
    font-family: "Lato", Arial, sans-serif;
  }
  .letterhead {
    position: absolute;
    left: 340px; top: 30px;
    width: 520px; height: 735px;
    background: var(--paper);
    box-shadow: 0 6px 24px rgba(0,0,0,0.12);
    overflow: hidden;
  }
  .brand {
    position: absolute; left: 34px; top: 34px;
    display: flex; align-items: center; gap: 12px;
  }
  .brand-square {
    width: 48px; height: 48px;
    border: 3px solid var(--brand-red);
    border-radius: 8px;
  }
  .brand-name {
    color: var(--ink-grey);
    font-weight: 400;
    font-size: 24px;
    line-height: 1.05;
    letter-spacing: 2px;
    text-transform: uppercase;
  }
  .watermark {
    position: absolute; left: 0; right: 0; top: 300px;
    text-align: center;
    color: var(--watermark);
    font-weight: 700;
    font-size: 62px;
    line-height: 1.05;
    letter-spacing: 3px;
    text-transform: uppercase;
  }
  .footer-swoosh {
    position: absolute; right: 0; bottom: 0;
    width: 300px; height: 120px;
  }
  .footer-tab {
    position: absolute; left: 0; bottom: 0;
    width: 74px; height: 9px;
    background: var(--brand-red);
    border-top-right-radius: 4px;
  }
  .contact {
    position: absolute; left: 40px; bottom: 22px;
    color: var(--soft-grey);
    font-size: 11px;
    line-height: 1.45;
  }
  .contact-row { display: flex; align-items: center; gap: 6px; }
  .contact-icon { width: 10px; height: 10px; fill: var(--brand-red); }
  .contact-web {
    color: var(--brand-red);
    font-weight: 700;
    margin-top: 2px;
  }
</style>
</head>
<body>
  <main class="letterhead">
    <header class="brand">
      <div class="brand-square"></div>
      <div class="brand-name">Maplerise<br>Trading</div>
    </header>

    <div class="watermark" aria-hidden="true">Maplerise<br>Trading</div>

    <svg class="footer-swoosh" viewBox="0 0 300 120" preserveAspectRatio="none" aria-hidden="true">
      <path d="M40 120 C150 110 250 70 300 10" fill="none" stroke="var(--soft-grey)" stroke-width="4"/>
      <path d="M70 120 C170 112 260 80 300 25 L300 120 Z" fill="var(--brand-red)"/>
    </svg>

    <footer class="contact">
      <div>48 Larchmont Ave, Suite 210</div>
      <div>Oakridge, ON L7K 3P2</div>
      <div class="contact-row">
        <svg class="contact-icon" viewBox="0 0 24 24"><path d="M6.6 10.8a15.1 15.1 0 0 0 6.6 6.6l2.2-2.2a1 1 0 0 1 1-.25 11.4 11.4 0 0 0 3.6.57 1 1 0 0 1 1 1V20a1 1 0 0 1-1 1A17 17 0 0 1 3 4a1 1 0 0 1 1-1h3.5a1 1 0 0 1 1 1c0 1.25.2 2.45.57 3.6a1 1 0 0 1-.25 1z"/></svg>
        <span>+1 (555) 304-2816</span>
        <svg class="contact-icon" viewBox="0 0 24 24"><path d="M2 5h20v14H2z M2 5l10 8 10-8" stroke="var(--paper)" stroke-width="1.5"/></svg>
        <span>info@mapleriseinc.com</span>
      </div>
      <div class="contact-web">www.mapleriseinc.ca</div>
    </footer>
    <div class="footer-tab"></div>
  </main>
</body>
</html>
```